Business Card for Graphic Design Firm

This project is for a new graphic design firm based in New Jersey called Velmoth. We outsource graphic design and marketing jobs. We want to communicate that this is a professional company but it as well creative and artistic. This card may be used as a horizontal double sided paper card or a vertical single sided translucent card so feel free to submit designs in whichever format or both.
Updates

Reason: Extending the deadline because I'm not exactly satisfied with the designs so far.

Please view the updated project brief

Target Market(s)

Adults aged 25-60

Industry/Entity Type

Graphic Design

Font styles to use
Serif
Sans Serif

Requirements
Nice to have
• Maybe a triangular pattern around the edges similar to our logo

```html
<!DOCTYPE html>
<html lang="en">
<head>
<meta charset="utf-8">
<title>Velmoth Business Card</title>
<link rel="stylesheet" href="https://fonts.googleapis.com/css2?family=Montserrat:wght@400;600&family=Varela+Round&display=swap">
<style>
  :root {
    --backdrop: #e9e8e6;
    --card: #ffffff;
    --teal-deep: #126c86;
    --teal: #14a3b8;
    --sky: #7ccbe8;
    --orange: #f0831f;
    --amber: #f8b12a;
    --slate: #6a6e70;
    --text-grey: #6d6e70;
  }
  html, body {
    margin: 0;
    padding: 0;
    width: 1200px;
    height: 1000px;
    overflow: hidden;
    background: var(--backdrop);
  }
  .canvas {
    position: relative;
    width: 1200px;
    height: 1000px;
  }
  .card {
    position: absolute;
    left: 265px;
    width: 665px;
    height: 397px;
    background: var(--card);
    box-shadow: 0 2px 6px rgba(0,0,0,0.18);
    overflow: hidden;
  }
  .card--front { top: 73px; }
  .card--back  { top: 533px; }

  .pattern-field { position: absolute; top: 0; bottom: 0; }
  .card--front .pattern-field--left {
    left: 0; width: 190px;
    background:
      linear-gradient(to right, rgba(255,255,255,0) 45%, var(--card) 100%),
      linear-gradient(to bottom, var(--teal) 0%, var(--amber) 28%, var(--teal-deep) 50%, var(--orange) 78%, var(--amber) 100%);
    opacity: 0.85;
  }
  .card--front .pattern-field--right {
    right: 0; width: 190px;
    background:
      linear-gradient(to left, rgba(255,255,255,0) 40%, var(--card) 100%),
      linear-gradient(to bottom, var(--teal-deep) 0%, var(--amber) 30%, var(--sky) 55%, var(--orange) 75%, var(--slate) 100%);
    opacity: 0.75;
  }
  .card--back .pattern-field--right {
    right: 0; width: 340px;
    background:
      linear-gradient(to left, rgba(255,255,255,0) 55%, var(--card) 100%),
      linear-gradient(to bottom, var(--teal) 0%, var(--orange) 30%, var(--teal-deep) 55%, var(--sky) 72%, var(--amber) 100%);
  }

  .brand-name {
    position: absolute;
    left: 0; right: 0;
    top: 236px;
    text-align: center;
    font-family: "Varela Round", "Montserrat", sans-serif;
    font-size: 46px;
    letter-spacing: 3px;
    color: var(--text-grey);
    margin: 0;
  }

  .identity { position: absolute; left: 33px; top: 95px; }
  .person-name {
    margin: 0;
    font-family: "Montserrat", sans-serif;
    font-weight: 600;
    font-size: 35px;
    line-height: 1;
    color: var(--teal-deep);
  }
  .person-name .surname { color: var(--text-grey); }
  .person-role {
    margin: 4px 0 0;
    font-family: "Montserrat", sans-serif;
    font-size: 16px;
    color: var(--teal-deep);
  }
  .contact-list {
    position: absolute;
    left: 33px; top: 181px;
    margin: 0; padding: 0;
    list-style: none;
    font-family: "Varela Round", sans-serif;
    font-size: 17px;
    color: var(--text-grey);
    line-height: 23px;
  }
  .contact-list li { display: flex; align-items: flex-start; gap: 8px; margin-bottom: 2px; }
  .contact-list svg { width: 15px; height: 15px; margin-top: 4px; fill: var(--teal-deep); flex: none; }
</style>
</head>
<body>
<div class="canvas">

  <section class="card card--front">
    <div class="pattern-field pattern-field--left" role="img" aria-label="Triangle mosaic in teal, sky blue, orange and grey"></div>
    <div class="pattern-field pattern-field--right" role="img" aria-label="Triangle mosaic in teal, sky blue, orange and grey fading toward the centre"></div>
    <h1 class="brand-name">VELMOTH</h1>
  </section>

  <section class="card card--back">
    <div class="identity">
      <h2 class="person-name">Mara <span class="surname">Lind</span></h2>
      <p class="person-role">Manager / CEO</p>
    </div>
    <ul class="contact-list">
      <li>
        <svg viewBox="0 0 16 16"><path d="M1 6c0-2 3-4 7-4s7 2 7 4l-1 1-3-1V5H5v1L2 7zM4 8h8l2 6H2z"/></svg>
        <span>+61 3 9000 4127</span>
      </li>
      <li>
        <svg viewBox="0 0 16 16"><path d="M1 3h14v10H1zM2 4l6 5 6-5v1L8 10 2 5z" fill-rule="evenodd"/></svg>
        <span>info@velmoth.com</span>
      </li>
      <li>
        <svg viewBox="0 0 16 16"><path d="M8 1a7 7 0 100 14A7 7 0 008 1zm0 1.5c.8 0 1.8 1.8 2 4.5H6c.2-2.7 1.2-4.5 2-4.5zM2.6 7h2.3c0-1.5.3-2.8.8-3.8A5.5 5.5 0 002.6 7zm8.5 0h2.3a5.5 5.5 0 00-3.1-3.8c.5 1 .8 2.3.8 3.8zM2.6 9a5.5 5.5 0 003.1 3.8c-.5-1-.8-2.3-.8-3.8zm3.4 0c.2 2.7 1.2 4.5 2 4.5s1.8-1.8 2-4.5zm5.1 0c0 1.5-.3 2.8-.8 3.8A5.5 5.5 0 0013.4 9z"/></svg>
        <span>www.velmoth.com</span>
      </li>
      <li>
        <svg viewBox="0 0 16 16"><path d="M8 1a5 5 0 00-5 5c0 4 5 9 5 9s5-5 5-9a5 5 0 00-5-5zm0 3a2 2 0 110 4 2 2 0 010-4z" fill-rule="evenodd"/></svg>
        <span>14 Calder Lane<br>Rowville VIC 3190</span>
      </li>
    </ul>
    <div class="pattern-field pattern-field--right" role="img" aria-label="Dense triangle mosaic in teal, sky blue, orange, amber and grey"></div>
  </section>

</div>
</body>
</html>
```